TovaLamarpe - Israeli Mental Health Website

We are developing an Israeli website for mental health. The website will be both in English and in Hebrew. We have a logo and would like a website design based on the logo and the logos colors (attached).

Attached is a doc that contains the website requirements.

We would like to have an icon for each of the sidebar categories, an image for each of the pages (including each of the sidebar category pages).

Target Market(s)

Adults 18-80

Industry/Entity Type

Mental Health

Number of Pages Required

5+ page

Font styles to use
Sans Serif

Colors

Designer to choose colors to be used in the design.

```html
<!DOCTYPE html>
<html lang="en">
<head>
<meta charset="utf-8">
<title>TovaLamarpe - Organization for Mental Health</title>
<link href="https://fonts.googleapis.com/css2?family=Archivo+Black&family=Arimo:wght@700&family=Poppins:wght@400;500;600;700&display=swap" rel="stylesheet">
<style>
:root{
  --green:#4fa845;
  --blue:#2a73c5;
  --blue-dark:#1f66b8;
  --ink:#222;
  --white:#fff;
  --muted:#e9e9e9;
}
*{box-sizing:border-box;margin:0;padding:0}
html,body{width:1200px;height:2558px;overflow:hidden;background:var(--white);font-family:'Poppins',sans-serif;color:var(--ink)}
.page{position:relative;width:1200px;height:2558px;overflow:hidden}
.abs{position:absolute}

.topbar{left:0;top:0;width:1200px;height:36px;background:var(--green)}
.lang{left:935px;top:0;width:154px;height:36px;background:var(--blue);color:var(--white);font-size:12px;font-weight:600;display:flex;align-items:center;justify-content:center}

.navbar{left:0;top:36px;width:1200px;height:70px;background:var(--white)}
.brand-disc{left:105px;top:2px;width:160px;height:146px;border-radius:50%;background:var(--white);z-index:5;display:flex;align-items:center;justify-content:center;gap:6px}
.brand-disc .dot{width:14px;height:14px;border-radius:50%;background:var(--green)}
.brand-disc span{font-weight:600;font-size:17px;color:var(--blue)}
.nav-call{left:453px;top:55px;width:33px;height:33px;border-radius:50%;background:var(--green);display:flex;align-items:center;justify-content:center}
.nav-links{left:515px;top:64px;display:flex;gap:26px;font-size:11.5px;font-weight:500;letter-spacing:.3px;color:#333}
.menu-btn{left:1028px;top:36px;width:60px;height:70px;background:#eef0f2;display:flex;align-items:center;justify-content:center}

.hero{left:0;top:106px;width:1200px;height:560px;background:linear-gradient(100deg,#3f6e8c 0%,#8a8a86 35%,#c9c3b9 60%,#9b9d9f 100%)}
.hero-title{left:110px;top:396px;font-family:'Archivo Black',sans-serif;font-size:55px;line-height:53px;color:var(--white)}

.dropdown{left:937px;top:118px;width:263px;height:534px;background:var(--white);border-radius:12px 0 0 12px;padding-top:26px;z-index:6;box-shadow:0 4px 14px rgba(0,0,0,.12)}
.dropdown li{list-style:none;display:flex;align-items:center;gap:12px;height:37.6px;padding-left:22px;font-size:12px;border-bottom:1px solid #f0f0f0}
.dropdown li svg{flex:none}
.dropdown li.active{background:var(--blue);color:var(--white);font-weight:600;margin-left:16px;padding-left:6px;border-radius:4px 0 0 4px;border:none}

.feature{background:linear-gradient(90deg,#2e4252 0%,#4c5d6a 45%,#36465a 100%);overflow:hidden}
.feature .scrim{position:absolute;inset:0;background:rgba(20,35,55,.25)}
.icon-circle{position:absolute;width:60px;height:60px;border-radius:50%;background:var(--green);display:flex;align-items:center;justify-content:center;box-shadow:0 0 0 6px rgba(79,168,69,.25)}
.card-title{font-family:'Arimo',sans-serif;font-weight:700;color:var(--white);font-size:27px;letter-spacing:.3px}
.card-text{color:var(--white);font-size:11px;line-height:16px}
.btn{position:absolute;background:var(--blue);color:var(--white);font-family:'Arimo',sans-serif;font-weight:700;font-size:12px;display:flex;align-items:center;justify-content:center;letter-spacing:.2px}

.tile{width:466px;height:438px;text-align:center}
.tile .icon-circle{left:203px;top:183px}
.tile .card-title{position:absolute;left:0;width:100%;top:259px}
.tile .card-text{position:absolute;left:60px;width:346px;top:305px;font-size:10.5px}
.tile .btn{height:40px;top:362px}

.footer{left:0;top:2228px;width:1200px;height:280px;background:var(--blue)}
.foot-brand{left:200px;top:2330px;color:var(--white);font-weight:600;font-size:24px;display:flex;align-items:center;gap:8px}
.foot-brand .dot{width:16px;height:16px;border-radius:50%;background:var(--white)}
.socials{left:232px;top:2420px;display:flex;gap:5px}
.socials span{width:36px;height:36px;border-radius:50%;background:var(--green);display:block}
.divider{width:1px;height:150px;background:rgba(255,255,255,.18);top:2306px}
.col h4{font-family:'Arimo',sans-serif;font-size:14px;color:var(--white);font-weight:700;padding-bottom:12px;border-bottom:1px solid rgba(255,255,255,.25);width:150px;margin-bottom:18px;position:relative}
.col h4::after{content:"";position:absolute;left:0;bottom:-1px;width:22px;height:2px;background:var(--green)}
.col li{list-style:none;color:#dce8f6;font-size:11px;line-height:21.5px}
.contact-row{display:flex;gap:8px;color:#dce8f6;font-size:11px;line-height:14px;margin-bottom:20px}
.contact-row.phone{color:var(--white);font-weight:700;font-size:12px}
.bottombar{left:0;top:2508px;width:1200px;height:50px;background:var(--green);color:var(--white);font-size:10.5px;display:flex;align-items:center;justify-content:center}
</style>
</head>
<body>
<div class="page">
  <div class="abs topbar"></div>
  <div class="abs lang">ENGLISH / אנגלית</div>

  <header class="abs navbar"></header>
  <div class="abs brand-disc"><i class="dot"></i><span>TovaLamarpe</span></div>
  <div class="abs nav-call">
    <svg width="16" height="16" viewBox="0 0 24 24"><path d="M6.6 10.8a15 15 0 006.6 6.6l2.2-2.2c.3-.3.7-.4 1-.2 1.1.4 2.3.6 3.6.6.6 0 1 .4 1 1V20c0 .6-.4 1-1 1A17 17 0 013 4c0-.6.4-1 1-1h3.5c.6 0 1 .4 1 1 0 1.3.2 2.5.6 3.6.1.3 0 .7-.2 1z" fill="#fff"/></svg>
  </div>
  <nav class="abs nav-links"><span>THERAPIST</span><span>ORGANIZATION</span><span>VIDEOS</span><span>CONTACT</span><span>ABOUT</span><span>DONATE</span></nav>
  <div class="abs menu-btn">
    <svg width="22" height="18" viewBox="0 0 22 18"><rect y="0" width="22" height="3" rx="1.5" fill="#2a73c5"/><rect y="7" width="22" height="3" rx="1.5" fill="#2a73c5"/><rect y="14" width="22" height="3" rx="1.5" fill="#2a73c5"/></svg>
  </div>

  <section class="abs hero" role="img" aria-label="Photo of a nurse talking with an older man on a sofa"></section>
  <h1 class="abs hero-title">TovaLamarpe<br>Organization for<br>Mental Health</h1>

  <ul class="abs dropdown">
    <li><svg width="18" height="18" viewBox="0 0 18 18" fill="none" stroke="#333" stroke-width="1.2"><circle cx="9" cy="6" r="4"/><path d="M3 16c1-3 3-4 6-4s5 1 6 4"/></svg>Emergency Mental Help</li>
    <li class="active"><svg width="18" height="18" viewBox="0 0 18 18" fill="none" stroke="#fff" stroke-width="1.2"><path d="M9 2v10"/><circle cx="9" cy="13" r="3"/></svg>Suicide</li>
    <li><svg width="18" height="18" viewBox="0 0 18 18" fill="none" stroke="#333" stroke-width="1.2"><circle cx="9" cy="5" r="3"/><rect x="4" y="9" width="10" height="7" rx="2"/></svg>Sexual Assault/violence Victims</li>
    <li><svg width="18" height="18" viewBox="0 0 18 18" fill="none" stroke="#333" stroke-width="1.2"><circle cx="9" cy="9" r="7"/><path d="M4 4l10 10"/></svg>Sexual Assault/violence Assaulters</li>
    <li><svg width="18" height="18" viewBox="0 0 18 18" fill="none" stroke="#333" stroke-width="1.2"><circle cx="9" cy="8" r="6"/><path d="M6 16h6"/></svg>Post Trauma</li>
    <li><svg width="18" height="18" viewBox="0 0 18 18" fill="none" stroke="#333" stroke-width="1.2"><circle cx="8" cy="5" r="3"/><path d="M4 16l3-7 5 2"/></svg>Depression</li>
    <li><svg width="18" height="18" viewBox="0 0 18 18" fill="none" stroke="#333" stroke-width="1.2"><circle cx="9" cy="10" r="5"/><path d="M3 3l2 2M15 3l-2 2M9 1v3"/></svg>Anxiety</li>
    <li><svg width="18" height="18" viewBox="0 0 18 18" fill="none" stroke="#333" stroke-width="1.2"><path d="M4 15V8a5 5 0 0110 0v2h-3v5"/></svg>Addictions</li>
    <li><svg width="18" height="18" viewBox="0 0 18 18" fill="none" stroke="#333" stroke-width="1.2"><rect x="3" y="2" width="12" height="14"/><path d="M6 7h6M6 11h6"/></svg>Sleep Disorders</li>
    <li><svg width="18" height="18" viewBox="0 0 18 18" fill="none" stroke="#333" stroke-width="1.2"><rect x="2" y="3" width="14" height="12" rx="2"/><circle cx="9" cy="9" r="3"/></svg>Eating Disorders</li>
    <li><svg width="18" height="18" viewBox="0 0 18 18" fill="none" stroke="#333" stroke-width="1.2"><circle cx="8" cy="4" r="2.5"/><circle cx="11" cy="12" r="4"/></svg>Financial Problems</li>
    <li><svg width="18" height="18" viewBox="0 0 18 18" fill="none" stroke="#333" stroke-width="1.2"><circle cx="5" cy="5" r="2.5"/><circle cx="13" cy="5" r="2.5"/><path d="M1 16v-5h8v5M9 16v-5h8v5"/></svg>Parenthood</li>
    <li><svg width="18" height="18" viewBox="0 0 18 18" fill="none" stroke="#333" stroke-width="1.2"><circle cx="5" cy="5" r="2.5"/><circle cx="13" cy="5" r="2.5"/><path d="M3 17v-8h4v8M11 17v-8h4v8"/></svg>Relationship</li>
  </ul>

  <section class="abs feature" style="left:110px;top:755px;width:980px;height:437px" role="img" aria-label="Photo of a distressed man holding a tissue to his face with a woman beside him">
    <div class="scrim"></div>
  </section>
  <div class="abs icon-circle" style="left:177px;top:838px">
    <svg width="30" height="30" viewBox="0 0 30 30" fill="none" stroke="#fff" stroke-width="1.8"><circle cx="17" cy="10" r="6"/><path d="M3 22h6l5 3h8l5-4M9 22v-4h6"/></svg>
  </div>
  <h2 class="abs card-title" style="left:176px;top:914px">EMERGENCY MENTAL HELP</h2>
  <p class="abs card-text" style="left:177px;top:955px;width:380px;font-size:12px;line-height:18px">Lorem Ipsum Dolor Sit Amet, Consectetur Adipiscing Elit, Sed Do Eiusmod Tempor Incididunt Ut Labore Et Dolore Magna Aliqua. Ut Enim Ad Minim Veniam, Quis Nostrud Exercitation Ullamco Laboris Nisi Ut Aliquip Ex Ea Commodo Consequat.</p>
  <div class="btn" style="left:177px;top:1046px;width:224px;height:40px">EMERGENCY MENTAL HELP</div>

  <section class="abs feature tile" style="left:110px;top:1240px" role="img" aria-label="Photo of a smiling woman holding up a large green message bubble">
    <div class="scrim"></div>
    <div class="icon-circle"><svg width="28" height="28" viewBox="0 0 24 24"><path d="M6.6 10.8a15 15 0 006.6 6.6l2.2-2.2c.3-.3.7-.4 1-.2 1.1.4 2.3.6 3.6.6.6 0 1 .4 1 1V20c0 .6-.4 1-1 1A17 17 0 013 4c0-.6.4-1 1-1h3.5c.6 0 1 .4 1 1 0 1.3.2 2.5.6 3.6.1.3 0 .7-.2 1z" fill="none" stroke="#fff" stroke-width="1.6"/></svg></div>
    <h2 class="card-title">SMART CHAT</h2>
    <p class="card-text">Lorem Ipsum Dolor Sit Amet, Consectetur Adipiscing Elit, Sed Do Eiusmod Tempor Incididunt Ut Labore Et Dolore Magna Aliqua. Ut Enim Ad Minim Veniam, Quis Nostrud Exercitat</p>
    <div class="btn" style="left:160px;width:144px">05X-XXXXXXX</div>
  </section>

  <section class="abs feature tile" style="left:624px;top:1240px" role="img" aria-label="Photo of a therapist guiding a woman through an arm stretch">
    <div class="scrim"></div>
    <div class="icon-circle"><svg width="30" height="30" viewBox="0 0 30 30" fill="none" stroke="#fff" stroke-width="1.8"><circle cx="9" cy="8" r="3"/><circle cx="21" cy="8" r="3"/><path d="M4 25V14h10v11M16 25V14h10v11"/></svg></div>
    <h2 class="card-title">THERAPISTS</h2>
    <p class="card-text">Lorem Ipsum Dolor Sit Amet, Consectetur Adipiscing Elit, Sed Do Eiusmod Tempor Incididunt Ut Labore Et Dolore Magna Aliqua. Ut Enim Ad Minim Veniam, Quis Nostrud Exercitation</p>
    <div class="btn" style="left:154px;width:158px">FIND THERAPISTS</div>
  </section>

  <section class="abs feature tile" style="left:110px;top:1724px" role="img" aria-label="Photo of a smiling group of colleagues at a meeting table">
    <div class="scrim"></div>
    <div class="icon-circle"><svg width="30" height="30" viewBox="0 0 30 30" fill="none" stroke="#fff" stroke-width="1.8"><path d="M15 12c-2-4-8-3-7 1 1 3 7 7 7 7s6-4 7-7c1-4-5-5-7-1z"/><path d="M3 10v8l6 7M27 10v8l-6 7"/></svg></div>
    <h2 class="card-title">ORGANIZATIONS</h2>
    <p class="card-text">Lorem Ipsum Dolor Sit Amet, Consectetur Adipiscing Elit, Sed Do Eiusmod Tempor Incididunt Ut Labore Et Dolore Magna Aliqua. Ut Enim Ad Minim Veniam, Quis Nostrud Exercitat</p>
    <div class="btn" style="left:138px;width:188px">FIND ORGANIZATIONS</div>
  </section>

  <section class="abs feature tile" style="left:624px;top:1724px" role="img" aria-label="Photo of a person watching a video call on a laptop">
    <div class="scrim"></div>
    <div class="icon-circle"><svg width="30" height="30" viewBox="0 0 30 30" fill="none" stroke="#fff" stroke-width="1.8"><rect x="4" y="7" width="22" height="16" rx="3"/><path d="M13 11l6 4-6 4z"/></svg></div>
    <h2 class="card-title">VIDEOS</h2>
    <p class="card-text">Lorem Ipsum Dolor Sit Amet, Consectetur Adipiscing Elit, Sed Do Eiusmod Tempor Incididunt Ut Labore Et Dolore Magna Aliqua. Ut Enim Ad Minim Veniam, Quis Nostrud Exercitation</p>
    <div class="btn" style="left:155px;width:156px">VIDEO LIBRARY</div>
  </section>

  <footer class="abs footer"></footer>
  <div class="abs foot-brand"><i class="dot"></i>TovaLamarpe</div>
  <div class="abs socials"><span></span><span></span><span></span></div>
  <div class="abs divider" style="left:415px"></div>
  <div class="abs divider" style="left:660px"></div>
  <div class="abs divider" style="left:843px"></div>

  <div class="abs col" style="left:454px;top:2316px">
    <h4>CONTACT US</h4>
    <div class="contact-row"><svg width="12" height="16" viewBox="0 0 12 16"><path d="M6 0a6 6 0 016 6c0 4-6 10-6 10S0 10 0 6a6 6 0 016-6z" fill="#fff"/><circle cx="6" cy="6" r="2" fill="#2a73c5"/></svg><span>Location name will be here<br>near this building 12345</span></div>
    <div class="contact-row phone"><svg width="14" height="14" viewBox="0 0 24 24"><path d="M6.6 10.8a15 15 0 006.6 6.6l2.2-2.2c.3-.3.7-.4 1-.2 1.1.4 2.3.6 3.6.6.6 0 1 .4 1 1V20c0 .6-.4 1-1 1A17 17 0 013 4c0-.6.4-1 1-1h3.5c.6 0 1 .4 1 1 0 1.3.2 2.5.6 3.6.1.3 0 .7-.2 1z" fill="#fff"/></svg><span>123-456-7890</span></div>
    <div class="contact-row"><svg width="14" height="11" viewBox="0 0 14 11"><rect width="14" height="11" fill="#fff"/><path d="M0 0l7 6 7-6" fill="none" stroke="#2a73c5"/></svg><span>info@TovaLamarpe.com</span></div>
  </div>
  <div class="abs col" style="left:701px;top:2316px">
    <h4>QUICK LINKS</h4>
    <ul><li>Smart Chat</li><li>Therapists</li><li>Organizations</li><li>Videos</li><li>Contact</li></ul>
  </div>
  <div class="abs col" style="left:883px;top:2316px">
    <h4>QUICK LINKS</h4>
    <ul><li>About</li><li>Donate</li><li>Privacy Policy</li><li>Terms-</li></ul>
  </div>

  <div class="abs bottombar">©2023 TovaLamarpe - Organization For Mental Health. All Rights Reserved.</div>
</div>
</body>
</html>
```